Rise As Captain Book Cover Design

Book Cover Design Brief
Book Title
Rise As Captain
Subtitle
The 12 Quiet Pillars of Remarkable Command
Author
Orwen Talbrisk
Overview
This book is about leadership that starts within.
Most leadership books focus on tactics or management strategies. This book focuses on the inner disciplines that create powerful leaders — mindset, integrity, focus, empathy, professionalism, honesty, and self-respect.
The tone of the book is bold, direct, confident, and transformational.
This is not a soft or corporate leadership book. It is a call to step up and become the leader you are capable of becoming.
The cover should feel:
• Powerful
• Professional
• Transformational
• Premium
• Memorable
Think best-selling leadership book, not a generic business book.
Target Audience
Business owners
Managers
Entrepreneurs
Team leaders
Professionals who want to grow as leaders
Most readers are ambitious professionals who want to level up their leadership and life.
Design Direction
The design should communicate:
Strength. Discipline. Leadership. Personal transformation.
Avoid cliché leadership visuals like:
• Handshakes
• Office buildings
• Corporate stock imagery
• Teams sitting around tables
The design should feel iconic, bold, and timeless.
Think about covers of successful leadership books such as:
Tiny Rituals
Total Custody
Won't Bend Now
Begin From Core
The 52 Codes of Sway
These covers are simple, powerful, and recognizable even at small sizes.
Typography
The title RISE AS CAPTAIN should be:
• Bold
• Strong
• Dominant on the cover
• Easy to read even at small sizes (important for Quillora thumbnails)
The subtitle should be clean and secondary to the title.
The overall typography should feel strong, modern, and premium.
Color Direction
Designers are free to explore colors, but the cover should feel strong and premium, not playful.
Colors that often work well for leadership books include:
Black
Gold
White
Deep blue
Dark red
High contrast and clarity are important.
Style
Preferred style:
• Clean
• Modern
• Minimal
• Strong contrast
Avoid clutter and overly busy designs.
The goal is to create a cover that feels powerful and professional at first glance.
Deliverables
Front cover design for a leadership book.
Final files should include:
• High resolution artwork
• Editable source files
• Print-ready version suitable for publishing
Goal of the Cover
When someone sees this book on Quillora or in a bookstore, they should immediately think:
“This looks like a serious leadership book.”
The design should feel like it belongs next to books by authors such as:
Marcus Dovell
Brant Feltham
Owen Marsh
Peter Halvorn
A strong, confident cover that attracts leaders who want to grow and perform at a higher level.
Updates
Target Market(s)
Business Owners and High level managers
Look and feel

```html
<!DOCTYPE html>
<html lang="en">
<head>
<meta charset="utf-8">
<title>Rise As Captain — Book Cover</title>
<link rel="stylesheet" href="https://fonts.googleapis.com/css2?family=Anton&family=Roboto+Condensed:wght@700&display=swap">
<style>
  :root {
    --page: #ffffff;
    --cover-red: #98272a;
    --gold: #cfa83d;
    --gold-dark: #a98633;
    --white: #ffffff;
    --edge: #2a1a1a;
  }
  html, body {
    margin: 0;
    padding: 0;
    width: 1200px;
    height: 1200px;
    overflow: hidden;
    background: var(--page);
  }
  .canvas {
    position: relative;
    width: 1200px;
    height: 1200px;
  }
  .cover {
    position: absolute;
    left: 243px;
    top: 58px;
    width: 669px;
    height: 1042px;
    background: var(--cover-red);
    box-shadow: 0 0 0 1px var(--edge);
  }
  .title-art {
    position: absolute;
    left: 0;
    top: 0;
    width: 1200px;
    height: 1200px;
  }
  .title-top {
    font-family: "Anton", "Oswald", sans-serif;
    fill: var(--white);
  }
  .title-main {
    font-family: "Anton", "Oswald", sans-serif;
    fill: var(--gold);
  }
  .subtitle {
    position: absolute;
    left: 243px;
    width: 669px;
    top: 938px;
    margin: 0;
    text-align: center;
    font-family: "Roboto Condensed", "Arial Narrow", sans-serif;
    font-weight: 700;
    font-size: 38px;
    line-height: 39px;
    color: var(--white);
    text-transform: uppercase;
    letter-spacing: 0.2px;
  }
  .author {
    position: absolute;
    left: 243px;
    width: 669px;
    top: 1046px;
    margin: 0;
    text-align: center;
    font-family: "Roboto Condensed", "Arial Narrow", sans-serif;
    font-weight: 700;
    font-size: 44px;
    line-height: 48px;
    color: var(--white);
    text-transform: uppercase;
    letter-spacing: 7px;
  }
</style>
</head>
<body>
<div class="canvas">
  <div class="cover"></div>

  <svg class="title-art" viewBox="0 0 1200 1200" xmlns="http://www.w3.org/2000/svg" aria-label="Rise As Captain">
    <defs>
      <linearGradient id="gold-bar" x1="0" y1="0" x2="1" y2="0">
        <stop offset="0" stop-color="var(--gold)"/>
        <stop offset="0.55" stop-color="var(--gold)"/>
        <stop offset="1" stop-color="var(--gold-dark)"/>
      </linearGradient>
    </defs>

    <g class="gold-bars" fill="url(#gold-bar)">
      <rect x="367" y="199" width="10" height="707"/>
      <rect x="389" y="168" width="10" height="738"/>
      <rect x="413" y="130" width="10" height="776"/>
      <rect x="740" y="130" width="10" height="776"/>
      <rect x="764" y="168" width="10" height="738"/>
      <rect x="786" y="199" width="10" height="707"/>
    </g>

    <text class="title-top" x="472" y="236" font-size="121" textLength="246" lengthAdjust="spacingAndGlyphs">RISE AS</text>

    <text class="title-main" transform="translate(456 254) rotate(90)" x="0" y="0" font-size="300" textLength="641" lengthAdjust="spacingAndGlyphs">CAPTAIN</text>
  </svg>

  <p class="subtitle">The 12 Quiet Pillars of<br>Remarkable Command</p>
  <p class="author">Orwen Talbrisk</p>
</div>
</body>
</html>
```